Business Card Design for ReaL ESTATE AGENT

New Business Cards for a real estate agent in Jacksonville, FL. My specialty is urban core, historic districts but sell through out the city. Company Name is Copper and Vale Realty a division of the Dunlow Companies. The card needs to convey an essence of professionalism, knowledge and success.

Target Market(s)

Home buyers and Sellers

Industry/Entity Type

Real Estate

Contact Information for Business Card

Double sided

Font styles to use
Sans Serif

Requirements
Must have
• My logs and photo (provided). My contact information as follows:
• Colin Marhoff
• Cell 904-618-3092
• Office 904-381-6247
• Email colinmarhoff@postwave.net
Nice to have
• Tag Line - Exceptional Effort. Proven Results.

```html
<!DOCTYPE html>
<html lang="en">
<head>
<meta charset="utf-8">
<title>Copper &amp; Vale Realty – Business Card</title>
<link rel="stylesheet" href="https://fonts.googleapis.com/css2?family=Open+Sans:wght@400;600;700&display=swap">
<style>
  :root {
    --bg: #e9e7e4;
    --card: #ffffff;
    --green: #1f6a4b;
    --orange: #ec5a3c;
    --portrait-top: #7d7f86;
    --portrait-bottom: #2c3038;
    --shadow: rgba(0, 0, 0, 0.18);
  }
  * { box-sizing: border-box; margin: 0; padding: 0; }
  html, body {
    width: 1200px;
    height: 844px;
    overflow: hidden;
    background: var(--bg);
    font-family: "Open Sans", sans-serif;
  }
  .stage {
    position: relative;
    width: 1200px;
    height: 844px;
  }
  .card {
    position: absolute;
    top: 267px;
    width: 525px;
    height: 310px;
    background: var(--card);
    box-shadow: 0 6px 18px var(--shadow);
    overflow: hidden;
  }
  .card--front { left: 50px; }
  .card--back { left: 625px; }

  .portrait {
    position: absolute;
    right: 0;
    bottom: 0;
    width: 215px;
    height: 272px;
    background: linear-gradient(180deg, var(--portrait-top) 0%, var(--portrait-bottom) 100%);
    border-top-left-radius: 100px 80px;
  }

  .identity {
    position: absolute;
    left: 34px;
    top: 170px;
  }
  .identity__name {
    color: var(--green);
    font-weight: 700;
    font-size: 22px;
    line-height: 1.1;
  }
  .identity__title {
    color: var(--orange);
    font-size: 14px;
    margin-top: 2px;
  }
  .contact {
    list-style: none;
    margin-top: 16px;
  }
  .contact__item {
    display: flex;
    align-items: center;
    gap: 7px;
    color: var(--orange);
    font-size: 15px;
    line-height: 1.5;
  }
  .contact__icon {
    width: 15px;
    height: 15px;
    flex: none;
  }

  .brand {
    position: absolute;
    inset: 0;
    display: flex;
    align-items: center;
    justify-content: center;
    gap: 14px;
  }
  .brand__mark {
    width: 34px;
    height: 34px;
    border: 4px solid var(--green);
  }
  .brand__name {
    color: var(--orange);
    font-weight: 700;
    font-size: 30px;
    letter-spacing: 0.5px;
  }
</style>
</head>
<body>
<main class="stage">
  <section class="card card--front">
    <div class="portrait" role="img" aria-label="Portrait photo of the agent in a dark suit and red tie"></div>
    <div class="identity">
      <h1 class="identity__name">Ellis Warrender</h1>
      <p class="identity__title">Managing Director</p>
      <ul class="contact">
        <li class="contact__item">
          <svg class="contact__icon" viewBox="0 0 16 16" aria-hidden="true">
            <rect width="16" height="16" rx="2" fill="var(--green)"/>
            <path d="M4 5.5c0-1 1-1.5 4-1.5s4 .5 4 1.5v1H10V5.8H6v.7H4z M4.5 7.5h7l.5 4.5h-8z" fill="#fff"/>
          </svg>
          044-517-2038
        </li>
        <li class="contact__item">
          <svg class="contact__icon" viewBox="0 0 16 16" aria-hidden="true">
            <rect width="16" height="16" rx="2" fill="var(--green)"/>
            <rect x="3.5" y="5" width="9" height="6.5" fill="none" stroke="#fff" stroke-width="1.2"/>
            <path d="M3.5 5l4.5 3.8L12.5 5" fill="none" stroke="#fff" stroke-width="1.2"/>
          </svg>
          hello@warrendermail.com
        </li>
      </ul>
    </div>
  </section>

  <section class="card card--back">
    <div class="brand">
      <span class="brand__mark" aria-hidden="true"></span>
      <span class="brand__name">Copper &amp; Vale Realty</span>
    </div>
  </section>
</main>
</body>
</html>
```